Business card design needed

I need a business card design for a dog walking, dog minding and dog training business. Please refer to my website for the basic company colours and fonts I'm after. Planning on a double sided card, so all information doesn't need to be on the 'front' side.
Cheers

Industry/Entity Type

Dog Training

Contact Information for Business Card

Bramble Paws - guiding hounds
Ned 0487306914
bramblepawsdemo.com.au
-walking
-holiday stays
-onsite care
-training and behavioural consultations

```html
<!DOCTYPE html>
<html lang="en">
<head>
<meta charset="utf-8">
<title>Bramble Paws – Business Card</title>
<link rel="stylesheet" href="https://fonts.googleapis.com/css2?family=Arvo:wght@700&family=Montserrat:wght@500;600&display=swap">
<style>
  :root {
    --backdrop: #6b3a22;
    --card-dark: #161616;
    --card-mid: #222222;
    --band-light: #f4f4f4;
    --band-edge: #dcdcdc;
    --accent: #e4472a;
    --accent-deep: #c6321b;
    --text-light: #ffffff;
    --rule: rgba(255,255,255,0.55);
    --photo-tone-a: #c98a52;
    --photo-tone-b: #f1ece4;
  }
  * { margin: 0; padding: 0; box-sizing: border-box; }
  html, body {
    width: 1200px; height: 1181px; overflow: hidden;
    background: var(--backdrop);
  }
  .stage { position: relative; width: 1200px; height: 1181px; }
  .card {
    position: absolute; left: 214px; width: 772px; height: 444px;
    background: radial-gradient(ellipse at 50% 40%, var(--card-mid), var(--card-dark) 75%);
    box-shadow: 0 6px 18px rgba(0,0,0,0.5);
    overflow: hidden;
  }
  .card--front { top: 109px; }
  .card--back { top: 618px; }
  .band {
    position: absolute; left: 0; top: 170px; width: 100%; height: 104px;
    background: radial-gradient(ellipse at 50% 50%, #ffffff, var(--band-light) 50%, var(--band-edge));
    box-shadow: 0 4px 10px rgba(0,0,0,0.45);
  }
  .photo-dog {
    position: absolute; left: 310px; top: 92px; width: 152px; height: 86px;
    border-radius: 60px 60px 6px 6px;
    background: radial-gradient(ellipse at 50% 45%, var(--photo-tone-b) 20%, var(--photo-tone-a) 70%);
    z-index: 2;
  }
  .brand-name {
    position: absolute; left: 0; top: 0; width: 100%; height: 104px;
    display: flex; align-items: center; justify-content: center;
    font-family: "Arvo", serif; font-weight: 700; font-size: 58px;
    letter-spacing: 1px; color: var(--accent); text-transform: uppercase;
  }
  .services {
    position: absolute; left: 234px; top: 290px; width: 304px; height: 40px;
    border-top: 1px solid var(--rule); border-bottom: 1px solid var(--rule);
    display: flex; flex-direction: column; justify-content: center; align-items: center;
    font-family: "Montserrat", sans-serif; font-weight: 500; font-size: 11.5px;
    line-height: 15px; color: var(--text-light);
  }
  .contact-row {
    position: absolute; left: 0; top: 0; width: 100%; height: 104px;
  }
  .person-name {
    position: absolute; left: 252px; top: 24px;
    font-family: "Arvo", serif; font-weight: 700; font-size: 52px; line-height: 56px;
    color: var(--accent); text-shadow: 0 2px 3px rgba(0,0,0,0.25);
  }
  .divider { position: absolute; left: 384px; top: 16px; }
  .contact-lines {
    position: absolute; left: 421px; top: 30px;
    font-family: "Montserrat", sans-serif; font-weight: 600; font-size: 17px;
    line-height: 21px; color: var(--accent); text-shadow: 0 1px 2px rgba(0,0,0,0.2);
  }
  .tagline {
    position: absolute; left: 0; top: 290px; width: 100%; text-align: center;
    font-family: "Montserrat", sans-serif; font-weight: 600; font-size: 17px;
    color: var(--text-light);
  }
</style>
</head>
<body>
<div class="stage">
  <section class="card card--front">
    <div class="photo-dog" role="img" aria-label="Photo of a small brown and white puppy peeking over the band"></div>
    <div class="band">
      <div class="brand-name">Bramble Paws</div>
    </div>
    <div class="services">
      <span>Walking - Holiday stays - Onsite care</span>
      <span>Training and Behavioural consultations</span>
    </div>
  </section>

  <section class="card card--back">
    <div class="band">
      <div class="contact-row">
        <div class="person-name">NED</div>
        <svg class="divider" width="6" height="72" viewBox="0 0 6 72" aria-hidden="true">
          <path d="M3 0 C4.5 24 4.5 48 3 72 C1.5 48 1.5 24 3 0 Z" fill="var(--accent-deep)"/>
        </svg>
        <div class="contact-lines">
          <div>0487306914</div>
          <div>bramblepawsdemo.com.au</div>
        </div>
      </div>
    </div>
    <div class="tagline">Guiding Hounds</div>
  </section>
</div>
</body>
</html>
```